Buch-/E-Book-Cover für Sachbuch über Hunderasse
Zielgruppe
Ich benötige ein Buch-Cover im DIN A5 Format für ein anspruchsvolles Sachbuch, das die rassetypischen Krankheiten der Hunderasse Rhodesian Ridgeback thematisiert. Die Zielgruppe sind Züchter, Tierärzte und Liebhaber der Rasse.
Aufgabenstellung
Den größten Raum sollte ein Foto der Rasse einnehmen. Das Foto würde ich stellen, im Entwurf kann also ein Beispielfoto verwendet werden. Da das Buch der Auftakt zu einer Reihe ist, sollte das Design einen hohen Wiedererkennungswert haben und in erster Linie seriös wirken. Das Foto, der Rassename und die verwendeten Farben sollten leicht austauschbar sein. Sowohl der Titel als auch der Untertitel sind recht lang. Der Arbeitstitel lautet: Der Rhodesian Ridgeback zwischen Sprechstunde und Alltag, Untertitel: Ein Begleiter für Halter und Praxisteams.

```html
<!DOCTYPE html>
<html lang="de">
<head>
<meta charset="utf-8">
<title>Buchcover – Der Rhodesian Ridgeback zwischen Sprechstunde und Alltag</title>
<link rel="stylesheet" href="https://fonts.googleapis.com/css2?family=Oswald:wght@400;500;700&family=Nunito+Sans:wght@300;400&display=swap">
<style>
  :root {
    --green: #b8d15a;
    --green-text: #b5cd55;
    --paper: #ffffff;
    --ink: #1b1b1b;
    --coat-dark: #8a4a1e;
    --coat: #b0652c;
    --coat-light: #c98543;
    --portrait-bg: #d9d6d1;
    --portrait-mid: #8c8f93;
  }
  * { box-sizing: border-box; margin: 0; padding: 0; }
  html, body { width: 1200px; height: 833px; overflow: hidden; background: var(--paper); }
  .cover-spread { position: relative; width: 1200px; height: 833px; background: var(--paper); overflow: hidden; }

  /* Hero photo area */
  .hero-photo {
    position: absolute; left: 420px; top: 255px; width: 780px; height: 370px;
    background:
      radial-gradient(ellipse 48% 45% at 72% 58%, var(--coat-light) 0%, var(--coat) 45%, transparent 80%),
      radial-gradient(ellipse 60% 50% at 45% 55%, var(--coat) 0%, var(--coat-dark) 55%, transparent 78%);
    opacity: .95;
  }

  /* Back cover */
  .author-panel {
    position: absolute; left: 115px; top: 127px; width: 311px; height: 509px;
    background: var(--green);
  }
  .author-portrait {
    position: absolute; left: 53px; top: 90px; width: 143px; height: 210px;
    background: linear-gradient(180deg, var(--portrait-bg) 0%, #c4c1bc 55%, var(--portrait-mid) 100%);
  }
  .author-text {
    position: absolute; color: #fff;
    font-family: "Nunito Sans", sans-serif; font-weight: 400;
    font-size: 11.4px; line-height: 15.7px; letter-spacing: -0.15px;
    text-align: justify; hyphens: auto; -webkit-hyphens: auto;
  }
  .author-text p + p { margin-top: 4px; }
  .author-text--intro { left: 227px; top: 186px; width: 181px; }
  .author-text--main { left: 139px; top: 329px; width: 269px; }

  /* Spine */
  .spine {
    position: absolute; left: 557px; top: 0; width: 62px; height: 833px;
    background: var(--green);
  }
  .spine-title {
    position: absolute; left: 0; top: 40px; width: 62px; height: 672px;
    writing-mode: vertical-rl; transform: rotate(180deg);
    font-family: "Oswald", sans-serif; color: #fff; white-space: nowrap;
    font-size: 21px; letter-spacing: .6px; line-height: 62px;
  }
  .spine-title strong { font-weight: 500; font-size: 27px; letter-spacing: 1.2px; }
  .spine-imprint {
    position: absolute; left: 0; bottom: 16px; width: 62px; text-align: center;
    font-family: "Oswald", sans-serif; font-weight: 700; color: var(--ink);
    font-size: 9.5px; line-height: 1.05; letter-spacing: .3px;
  }

  /* Front cover */
  .front-title {
    position: absolute; right: 42px; top: 60px; text-align: right;
    font-family: "Oswald", sans-serif; color: var(--green-text); line-height: 1;
    font-weight: 500;
  }
  .front-title__lead { font-size: 32px; letter-spacing: 1.5px; margin-right: 8px; }
  .front-title__breed { font-size: 44px; letter-spacing: 1.5px; }
  .front-title__line2 { display: block; margin-top: 14px; font-size: 32px; font-weight: 400; letter-spacing: 1.5px; }
  .front-subtitle {
    position: absolute; left: 721px; top: 722px;
    font-family: "Oswald", sans-serif; font-weight: 400; color: var(--green-text);
    font-size: 30px; line-height: 40px; letter-spacing: .8px;
  }
  .front-imprint {
    position: absolute; left: 1080px; top: 762px; width: 100px; text-align: center;
    font-family: "Oswald", sans-serif; font-weight: 700; color: var(--ink);
    font-size: 15px; line-height: 1.1; letter-spacing: .5px;
  }
  .front-imprint__mark { display: block; width: 22px; height: 22px; margin: 0 auto 6px; background: var(--ink); }
</style>
</head>
<body>
<main class="cover-spread">
  <div class="hero-photo" role="img" aria-label="Foto eines liegenden Rhodesian Ridgeback, rotbraunes Fell, Kopf auf den Vorderpfoten, vor weißem Hintergrund"></div>

  <section class="back-cover">
    <div class="author-panel"></div>
    <div class="author-portrait" role="img" aria-label="Porträtfoto des Autors"></div>
    <div class="author-text author-text--intro">
      <p>In den 25 Jahren meiner selbst&shy;ändigen Arbeit als Hebamme, habe ich viele Familien im Wochenbett betreut und dabei einen reichen Erfahrungsschatz gesammelt. Meine häufigsten Kunden waren natürlich Familien, die das erste Kind bekommen haben.</p>
    </div>
    <div class="author-text author-text--main">
      <p>Dies war zu der Zeit, als gerade der Krankenhaus&shy;aufenthalt nach einer Spontangeburt von zehn auf sieben Tage gekürzt worden war. Die Kran&shy;kenkasse bezahlte im Anschluss daran vier Tage Hebammen- Betreuung. Wenn die Familie diver&shy;se schwierige Themenfelder hatte, übernahm die Kasse die Kosten auch länger.</p>
      <p>Da ich meinen Beruf liebte, nahm ich mir für den Wochenbettbesuch auch immer genügend Zeit. Meist war eine Stunde nötig, manchmal jedoch waren so viele Fragen oder Irritationen (Unklar&shy;heiten), daß ich länger blieb. Auf die frisch geba&shy;ckenen Eltern kommen unzählige unbekannte Si&shy;tuationen zu, die total verunsichern können. Auch bei sehr einfühlsamer Betreuung im Krankenhaus stellen sich viele Fragen erst zu Hause. Nämlich dann, wenn der Alltag mit dem Baby beginnt.</p>
    </div>
  </section>

  <aside class="spine">
    <div class="spine-title">Der&nbsp;<strong>RHODESIAN RIDGEBACK</strong>&nbsp;zwischen Sprechstunde und Alltag</div>
    <div class="spine-imprint">PRAXIS-<br>REIHE</div>
  </aside>

  <section class="front-cover">
    <h1 class="front-title">
      <span class="front-title__lead">Der</span><span class="front-title__breed">RHODESIAN RIDGEBACK</span>
      <span class="front-title__line2">zwischen Sprechstunde und Alltag</span>
    </h1>
    <p class="front-subtitle">Ein Begleiter für Halter<br>und Praxisteams</p>
    <div class="front-imprint"><span class="front-imprint__mark"></span>PRAXISREIHE</div>
  </section>
</main>
</body>
</html>
```